Business Card Re-Design/Update

We'd like to update out business cards. I've included our current "Style guide" which has the colour scheme of the organisation in it. I've also included the branding files with logos etc in them.

I've also included a copy of one of our existing cards so that you can see how ugly/dated they look. I'd like a fresh modern corporate look.

Target Market(s)

These are for our clients, potential clients, industry contacts - like all business cards

Contact Information for Business Card

Name
Position
Company Address - Level 1, 47 Garnet Lane, Toowong Qld 4066
Direct Phone
mobile
Email
Website -www.korvalnet.com.au
Logo

Colors

Designer to choose colors to be used in the design.

Requirements
Must have
• Main Logo
• Cards will need to be editable to be able to personalize them for each new employee.
Nice to have
• The MapOUT, HandOVER, UpKEEP would be okay to have if they can be sensibly and professionally added to the look without detracting from the main imagery.
• Maybe they could go on the back of the card? will leave this to your creative discretion as to whether/where they fit.
Should not have
• Should not have decorative or script fonts

```html
<!DOCTYPE html>
<html lang="en">
<head>
<meta charset="utf-8">
<title>korvalnet business card</title>
<link href="https://fonts.googleapis.com/css2?family=Lato:wght@400;700;900&display=swap" rel="stylesheet">
<style>
  :root {
    --backdrop: #1f1f20;
    --red: #d4212b;
    --red-deep: #a8141c;
    --red-light: #e43a3c;
    --white: #ffffff;
    --paper: #f2f2f2;
    --ink: #2a2a2c;
    --soft: #f4c9cb;
  }
  * { margin: 0; padding: 0; box-sizing: border-box; }
  html, body { width: 1200px; height: 997px; overflow: hidden; }
  body {
    background: var(--backdrop);
    font-family: "Lato", Arial, sans-serif;
    position: relative;
  }
  .card {
    position: absolute;
    top: 344px;
    width: 540px;
    height: 309px;
    overflow: hidden;
    box-shadow: 0 10px 30px rgba(0,0,0,.5);
  }
  .card-front { left: 40px; }
  .card-back { left: 620px; background: var(--paper); }

  /* front */
  .front-pattern {
    position: absolute; inset: 0;
    background: linear-gradient(135deg, var(--red-light) 0%, var(--red) 50%, var(--red-deep) 100%);
  }
  .front-brand {
    position: absolute; left: 0; right: 0; top: 108px;
    display: flex; align-items: center; justify-content: center; gap: 16px;
  }
  .brand-square { width: 46px; height: 46px; background: var(--white); }
  .front-brand .brand-name {
    font-weight: 700; font-size: 62px; color: var(--ink); letter-spacing: -1px; line-height: 1;
  }
  .front-web {
    position: absolute; left: 0; right: 0; top: 196px; text-align: center;
    color: var(--white); font-size: 13px; font-weight: 700; letter-spacing: 6px; text-transform: uppercase;
  }

  /* back */
  .back-top { position: absolute; left: 0; top: 0; width: 540px; height: 148px; background: var(--paper); }
  .back-brand {
    position: absolute; left: 34px; top: 92px;
    display: flex; align-items: center; gap: 10px;
  }
  .back-brand .brand-square { width: 26px; height: 26px; background: var(--red); }
  .back-brand .brand-name { font-weight: 700; font-size: 38px; color: var(--ink); letter-spacing: -.5px; line-height: 1; }
  .stripe { position: absolute; left: 0; width: 540px; background: var(--red); }
  .stripe-1 { top: 150px; height: 3px; }
  .stripe-2 { top: 157px; height: 3px; }
  .back-red {
    position: absolute; left: 0; top: 164px; width: 540px; height: 145px;
    background: linear-gradient(180deg, var(--red) 0%, var(--red-deep) 100%);
  }
  .person { position: absolute; right: 290px; top: 18px; text-align: right; color: var(--white); }
  .person-name { font-weight: 700; font-size: 15px; letter-spacing: .5px; text-transform: uppercase; }
  .person-role { font-size: 12px; color: var(--soft); margin-top: 2px; }
  .address { margin-top: 20px; font-weight: 700; font-size: 13px; line-height: 1.35; }
  .divider {
    position: absolute; left: 268px; top: 14px; width: 2px; height: 110px;
    background: linear-gradient(180deg, transparent, rgba(0,0,0,.45), transparent);
  }
  .contacts { position: absolute; left: 292px; top: 16px; list-style: none; color: var(--white); font-size: 12.5px; }
  .contacts li { display: flex; align-items: center; gap: 10px; height: 24px; }
  .contacts svg { width: 13px; height: 13px; fill: var(--white); flex: none; }
  .contacts .note { font-size: 10.5px; color: var(--soft); margin-left: 4px; }
</style>
</head>
<body>
  <section class="card card-front">
    <div class="front-pattern" role="img" aria-label="Faceted low-poly red background pattern"></div>
    <div class="front-brand">
      <span class="brand-square"></span>
      <span class="brand-name">korvalnet</span>
    </div>
    <p class="front-web">www.korvalnet.com.au</p>
  </section>

  <section class="card card-back">
    <div class="back-top"></div>
    <div class="back-brand">
      <span class="brand-square"></span>
      <span class="brand-name">korvalnet</span>
    </div>
    <div class="stripe stripe-1"></div>
    <div class="stripe stripe-2"></div>
    <div class="back-red">
      <div class="person">
        <p class="person-name">Dana Whitlow</p>
        <p class="person-role">Business Development Manager</p>
        <p class="address">Level 1, 47 Garnet Lane<br>Toowong QLD 4066</p>
      </div>
      <div class="divider"></div>
      <ul class="contacts">
        <li><svg viewBox="0 0 16 16"><path d="M1 5c0-2 3-3 7-3s7 1 7 3v1h-4V4.5H5V6H1zM3 7h10l1 7H2z"/></svg>+61 (0)412 555 019</li>
        <li><svg viewBox="0 0 16 16"><path d="M4 1h8v4H4zM1 6h14v6h-3v3H4v-3H1zm4 4v4h6v-4z"/></svg>+61 (0)7 3000 1100</li>
        <li><svg viewBox="0 0 16 16"><path d="M3 1l3 3-2 2c1 2 4 5 6 6l2-2 3 3-2 2C7 15 1 9 1 3z"/></svg>+61 (0)7 3000 1122<span class="note">(Direct)</span></li>
        <li><svg viewBox="0 0 16 16"><path d="M1 3h14v10H1zm1 1.5v.3L8 9l6-4.2v-.3z"/></svg>dwhitlow@korvalnet.com.au</li>
      </ul>
    </div>
  </section>
</body>
</html>
```